VORN Paradigm. the way you communicate in every situation and in all environments.

I would like you to create a diagram depicting a very specific process of communication. it must follow the look of the diagram that i have attached. this is going to be used in a book called LANTERN. it is going to explain the fact that we communicate all the same way using this process as we communicate. it starts with the fact that everyone takes everything that is said personally and then moves on to filters, which is your own agenda or experience kicking in. then you move to your why it matters, which is your motivation and ends with the choice of words you use when you communicate. if you are going to be successful then you must separate the person from the issue.

Target Market(s)

market is executive business people around the world

Industry/Entity Type

Consulting

Font styles to use
Sans Serif

Colors

Designer to choose only greyscale colors for use in the design.

Requirements
Must have
• I would like it to have a diving/ocean/snorkel feel to it. The analogy we are using is to make a deep dive when you are communicating. it must have every part of the diagram you see, it starts at the top with the vorn paradigm (and the words) it then connects to the filters which connects to the why it matters with connects to the words and then end with the separating the person from the issue.
Nice to have
• we are writing a black and white book NO color. therefore the words should be clear and easy to read. Each section should be able to stand on its own so we can write about it separately.
Should not have
• the diagram DOES NOT have to look like the one i gave you. it must explain the fact that it starts with VORN and ends with Separate and must pass through the three areas to get to the SEPARATE.

```html
<!DOCTYPE html>
<html lang="en">
<head>
<meta charset="utf-8">
<title>VORN Paradigm — Communication Diagram</title>
<link href="https://fonts.googleapis.com/css2?family=Montserrat:wght@600;700&family=Roboto:wght@400;700&display=swap" rel="stylesheet">
<style>
  :root{
    --page:#efefef;
    --halo:#f5f5f5;
    --halo-edge:#d6d6d6;
    --ink:#111111;
    --ring:#0d0d0d;
    --bowl-dark:#9a9a9a;
    --bowl-light:#cfcfcf;
    --inner:#f7f7f7;
    --icon-bg:#d9d9d9;
    --white:#ffffff;
  }
  html,body{margin:0;padding:0;width:1180px;height:1200px;overflow:hidden;background:var(--page);}
  .diagram{display:block;width:1180px;height:1200px;}
  .ring-title{font-family:"Montserrat",sans-serif;font-weight:700;fill:var(--white);letter-spacing:.5px;}
  .body-text{font-family:"Roboto",sans-serif;fill:var(--ink);text-anchor:middle;}
  .body-text .strong{font-weight:700;}
  .book-title{font-family:"Montserrat",sans-serif;font-weight:600;fill:var(--white);font-size:21px;letter-spacing:12px;text-anchor:middle;}
  .chev{fill:none;stroke:var(--ink);stroke-width:2.4;stroke-linecap:round;stroke-linejoin:round;}
  .connector{fill:none;stroke:var(--ink);stroke-width:2.6;}
  .icon-bg{fill:var(--icon-bg);}
  .icon{fill:var(--ink);}
  .icon-line{fill:none;stroke:var(--ink);stroke-width:2.6;stroke-linecap:round;}
</style>
</head>
<body>
<svg class="diagram" viewBox="307 235 783 1025" preserveAspectRatio="xMidYMid meet" role="img" aria-label="VORN Paradigm communication process: VORN Paradigm, your filters, why it matters, your words, what to do">
  <defs>
    <path id="arc-vorn" d="M617,455 A71,71 0 0 1 759,455"/>
    <path id="arc-filters" d="M407,593 A62,62 0 0 1 531,593"/>
    <path id="arc-why" d="M621,742 A67,67 0 0 1 755,742"/>
    <path id="arc-words" d="M854,885 A62,62 0 0 1 978,885"/>
    <path id="arc-todo" d="M612,1030 A76,76 0 0 1 764,1030"/>
  </defs>

  <!-- top rule -->
  <line x1="364" y1="314" x2="1038" y2="314" stroke="var(--ink)" stroke-width="2.5"/>

  <!-- halos: outline layer -->
  <g class="halo-edges" fill="var(--halo-edge)">
    <circle cx="688" cy="455" r="101"/>
    <circle cx="469" cy="593" r="87"/>
    <circle cx="688" cy="742" r="87"/>
    <circle cx="916" cy="885" r="82"/>
    <circle cx="688" cy="1030" r="101"/>
    <path d="M469,593 C560,680 600,700 688,742 C780,790 820,840 916,885" fill="none" stroke="var(--halo-edge)" stroke-width="63"/>
  </g>
  <!-- halos: fill layer -->
  <g class="halo-fills" fill="var(--halo)">
    <circle cx="688" cy="455" r="99"/>
    <circle cx="469" cy="593" r="85"/>
    <circle cx="688" cy="742" r="85"/>
    <circle cx="916" cy="885" r="80"/>
    <circle cx="688" cy="1030" r="99"/>
    <path d="M469,593 C560,680 600,700 688,742 C780,790 820,840 916,885" fill="none" stroke="var(--halo)" stroke-width="60"/>
  </g>

  <!-- step: VORN Paradigm -->
  <g class="step">
    <circle cx="688" cy="455" r="80" fill="var(--ring)"/>
    <circle cx="688" cy="455" r="62" fill="var(--bowl-dark)"/>
    <circle cx="688" cy="455" r="55" fill="var(--bowl-light)"/>
    <ellipse cx="688" cy="440" rx="52" ry="50" fill="var(--inner)"/>
    <text class="ring-title" font-size="17"><textPath href="#arc-vorn" startOffset="50%" text-anchor="middle" dominant-baseline="middle">VORN PARADIGM</textPath></text>
    <text class="body-text" font-size="13">
      <tspan x="688" y="414">When</tspan><tspan x="688" y="430">words are</tspan><tspan x="688" y="446">taken</tspan><tspan x="688" y="462">personally,</tspan><tspan x="688" y="478" class="strong">What</tspan><tspan x="688" y="494" class="strong">happens?</tspan>
    </text>
  </g>

  <!-- step: Your Filters -->
  <g class="step">
    <circle cx="469" cy="593" r="70" fill="var(--ring)"/>
    <circle cx="469" cy="593" r="54" fill="var(--bowl-dark)"/>
    <circle cx="469" cy="593" r="48" fill="var(--bowl-light)"/>
    <ellipse cx="469" cy="580" rx="45" ry="43" fill="var(--inner)"/>
    <text class="ring-title" font-size="15"><textPath href="#arc-filters" startOffset="50%" text-anchor="middle" dominant-baseline="middle">YOUR FILTERS</textPath></text>
    <text class="body-text" font-size="10">
      <tspan x="469" y="565">An</tspan><tspan x="469" y="577">accumulation</tspan><tspan x="469" y="589">of your</tspan><tspan x="469" y="601" class="strong">experience,</tspan><tspan x="469" y="613" class="strong">knowledge and</tspan><tspan x="469" y="625" class="strong">value</tspan>
    </text>
  </g>

  <!-- step: Why It Matters -->
  <g class="step">
    <circle cx="688" cy="742" r="75" fill="var(--ring)"/>
    <circle cx="688" cy="742" r="58" fill="var(--bowl-dark)"/>
    <circle cx="688" cy="742" r="51" fill="var(--bowl-light)"/>
    <ellipse cx="688" cy="728" rx="49" ry="46" fill="var(--inner)"/>
    <text class="ring-title" font-size="15"><textPath href="#arc-why" startOffset="50%" text-anchor="middle" dominant-baseline="middle">WHY IT MATTERS</textPath></text>
    <text class="body-text" font-size="10">
      <tspan x="688" y="726">This is your</tspan><tspan x="688" y="739">compass, It is <tspan class="strong">What</tspan></tspan><tspan x="688" y="752" class="strong">motivates you,</tspan><tspan x="688" y="765" class="strong">What drives you.</tspan>
    </text>
  </g>

  <!-- step: Your Words -->
  <g class="step">
    <circle cx="916" cy="885" r="70" fill="var(--ring)"/>
    <circle cx="916" cy="885" r="54" fill="var(--bowl-dark)"/>
    <circle cx="916" cy="885" r="48" fill="var(--bowl-light)"/>
    <ellipse cx="916" cy="872" rx="45" ry="43" fill="var(--inner)"/>
    <text class="ring-title" font-size="15"><textPath href="#arc-words" startOffset="50%" text-anchor="middle" dominant-baseline="middle">YOUR WORDS</textPath></text>
    <text class="body-text" font-size="10">
      <tspan x="908" y="869">This is</tspan><tspan x="908" y="881">your immediate</tspan><tspan x="908" y="893">response,</tspan><tspan x="908" y="905" class="strong">verbal or perhaps</tspan><tspan x="908" y="917" class="strong">non-verbal.</tspan>
    </text>
  </g>

  <!-- step: What To Do -->
  <g class="step">
    <circle cx="688" cy="1030" r="85" fill="var(--ring)"/>
    <circle cx="688" cy="1030" r="66" fill="var(--bowl-dark)"/>
    <circle cx="688" cy="1030" r="58" fill="var(--bowl-light)"/>
    <ellipse cx="688" cy="1014" rx="56" ry="53" fill="var(--inner)"/>
    <text class="ring-title" font-size="18"><textPath href="#arc-todo" startOffset="50%" text-anchor="middle" dominant-baseline="middle">WHAT TO DO</textPath></text>
    <text class="body-text strong" font-size="16" font-weight="700">
      <tspan x="688" y="1007">Separate</tspan><tspan x="688" y="1028">the person</tspan><tspan x="688" y="1048">from</tspan><tspan x="688" y="1068">the issue</tspan>
    </text>
  </g>

  <!-- connectors -->
  <g class="connectors">
    <path class="connector" d="M590,453 L520,453 C485,453 466,475 466,507"/>
    <circle cx="590" cy="453" r="6" fill="var(--ink)"/>
    <circle cx="466" cy="507" r="6" fill="var(--ink)"/>
    <path class="chev" d="M530,447 l-6,6 l6,6 M539,447 l-6,6 l6,6 M548,447 l-6,6 l6,6"/>

    <path class="connector" d="M913,981 C913,1015 895,1035 860,1035 L790,1035"/>
    <circle cx="913" cy="981" r="6" fill="var(--ink)"/>
    <circle cx="790" cy="1035" r="6" fill="var(--ink)"/>
    <path class="chev" d="M838,1029 l-6,6 l6,6 M847,1029 l-6,6 l6,6 M856,1029 l-6,6 l6,6"/>

    <path class="chev" d="M560,657 l7,5 l-5,7 M569,659 l7,5 l-5,7 M578,661 l7,5 l-5,7"/>
    <path class="chev" d="M781,807 l7,5 l-5,7 M790,809 l7,5 l-5,7 M799,811 l7,5 l-5,7"/>
  </g>

  <!-- icons -->
  <g class="icons">
    <!-- bulb -->
    <circle class="icon-bg" cx="430" cy="465" r="29"/>
    <circle class="icon" cx="430" cy="460" r="11"/>
    <rect class="icon" x="424" y="471" width="12" height="4" rx="1"/>
    <rect class="icon" x="425" y="477" width="10" height="3" rx="1"/>
    <!-- share nodes -->
    <circle class="icon-bg" cx="835" cy="455" r="29"/>
    <path class="icon-line" d="M823,461 L836,446 M823,461 L845,466"/>
    <circle class="icon" cx="836" cy="444" r="5"/>
    <circle class="icon" cx="822" cy="462" r="5"/>
    <circle class="icon" cx="847" cy="467" r="5"/>
    <!-- compass -->
    <circle class="icon-bg" cx="771" cy="636" r="29"/>
    <circle cx="771" cy="636" r="13" fill="none" stroke="var(--ink)" stroke-width="2.6"/>
    <path class="icon" d="M779,628 L774,639 L763,644 L768,633 Z"/>
    <!-- speech bubble -->
    <circle class="icon-bg" cx="990" cy="787" r="29"/>
    <ellipse class="icon" cx="990" cy="785" rx="14" ry="11"/>
    <path class="icon" d="M982,792 L979,802 L990,794 Z"/>
    <!-- double arrow -->
    <circle class="icon-bg" cx="541" cy="1031" r="29"/>
    <path class="icon-line" d="M527,1031 L555,1031"/>
    <path class="icon" d="M522,1031 L531,1024 L531,1038 Z M560,1031 L551,1024 L551,1038 Z"/>
  </g>

  <!-- book title band -->
  <rect x="364" y="1171" width="674" height="32" fill="var(--ink)"/>
  <text class="book-title" x="706" y="1195">LANTERN</text>
</svg>
</body>
</html>
```